Web Design: Tovel Crowdfunding Platform

Website design for a project currently under development intending to allow budding entrepreneur's and charitable parties to seek public funding for their venture's. The platform is planned to operate in a similar way to ArtHive, with entrepreneur's and supporters. For details of how this sort of platform operates, you can check the brivopedia page [en.brivopedia.example/wiki/Crowd_funding].

An overview of the workflow;
1. Entrepreneur creates a venture.
2. Supporters discover venture and decide to support it.
3. Supporter commits to makes a payment commitment via some merchant gateway.
4. When the venture end time arrives, everyone involved is notified regarding the success or abandonment of the venture.
5. In the case of a successful funding raise;
5.1 Supporter payments are processed and approved or rejected.
5.2 Entrepreneur proceeds to contact all approved supporters in order to complete their pledges.

We have no existing branding for this product, so website design will include logo design. Something simple will most likely work best. We are using the name "Tovel Crowdunding" currently.

Will want to see your ideas for a few pages. In particular, the home page of course, a category/search page and a details page for a particular venture. We will attach screenshots of our working prototype, they give an idea of the layout we are currently working with. You will probably recognise the standard jQuery UI theme currently used. If you can design something nice within the jQuery UI framework, that's great, but it is probably too restricting.

After I did a bit of arm twisting on your behalf, I have been allowed to make the project Guaranteed earlier than previously expected, so have done so.

Appreciate your input!

Industry/Entity Type

Crowdfunding

Requirements
Should not have
• We would like to avoid loading/splash pages or anything that would slow down a user's initial experience. Minimise clicks from being new entrepreneur to getting a project going.

Avoid distracting animations [transition effects, appropriately used are effective].

```html
<!DOCTYPE html>
<html lang="en">
<head>
<meta charset="utf-8">
<title>Tovel CrowdFunding</title>
<link href="https://fonts.googleapis.com/css2?family=Arimo:wght@400;700&display=swap" rel="stylesheet">
<style>
:root{
  --navy-deep:#0e2236;
  --navy-mid:#1d4268;
  --ink:#13263a;
  --panel:#ffffff;
  --tile:#ebebeb;
  --login-bg:#8b9197;
  --btn-top:#34404d;
  --btn-bottom:#111a24;
  --green-top:#b0d660;
  --green-bottom:#6f9e22;
  --teal-top:#62e6e0;
  --teal-bottom:#1ca9a6;
  --orange-top:#ffb85a;
  --orange-bottom:#d77814;
  --stripe-dark:#241c3d;
  --stripe-light:#d8d6e8;
  --track:#cfcfcf;
}
*{box-sizing:border-box;margin:0;padding:0}
html,body{width:1200px;height:900px;overflow:hidden}
body{position:relative;font-family:"Arimo",Arial,sans-serif;color:var(--ink);
  background:linear-gradient(#c8c8c8 413px,#f6f6f6 860px)}
.masthead{position:absolute;left:0;top:0;width:1200px;height:413px;
  background:radial-gradient(ellipse 600px 380px at 560px 60px,var(--navy-mid),var(--navy-deep))}
.brand{position:absolute;left:126px;top:44px;display:flex;align-items:center;gap:16px}
.brand-mark{width:42px;height:42px;border-radius:50%;background:#f5a21c}
.brand-name{font-weight:700;font-size:28px;color:#fff;letter-spacing:.3px}
.login{position:absolute;left:646px;top:42px;width:395px;height:44px;border-radius:8px;background:var(--login-bg)}
.login .field{position:absolute;top:13px;height:20px;background:#fff;border:1px solid #b8bcc0;
  font-size:13px;color:#8c9196;padding:2px 7px;letter-spacing:.5px}
.login .email{left:11px;width:158px}
.login .password{left:181px;width:125px}
.login .go{position:absolute;left:317px;top:13px;width:67px;height:20px;border-radius:4px;
  background:linear-gradient(var(--btn-top),var(--btn-bottom));color:#fff;font-size:13px;text-align:center;line-height:20px}
.nav a{position:absolute;top:122px;color:#fff;font-weight:700;font-size:15px;letter-spacing:.4px;text-decoration:none;transform:translateX(-50%)}
.nav .home{left:125px;top:110px;width:131px;height:42px;transform:none;border-radius:6px 6px 0 0;
  background:linear-gradient(#9aa1a8,#fff 70%);color:var(--ink);font-size:18px;text-align:center;padding-top:10px}
.sheet{position:absolute;left:115px;top:151px;width:929px;height:709px;background:var(--panel);
  border-radius:8px 8px 0 0;box-shadow:0 0 12px rgba(0,0,0,.25)}
.promo{position:absolute;top:191px;width:208px;height:208px;border:2px solid #fff;border-radius:8px;
  box-shadow:3px 4px 6px rgba(0,0,0,.45)}
.promo h2{position:absolute;z-index:1;left:11px;top:9px;font-size:18px;line-height:24px;letter-spacing:.8px;color:var(--ink)}
.promo .art{position:absolute}
.promo .cta{position:absolute;left:16px;top:157px;width:175px;height:32px;border-radius:3px;
  background:linear-gradient(var(--btn-top),var(--btn-bottom));color:#fff;font-weight:700;font-size:13px;
  text-align:center;line-height:32px;letter-spacing:.3px}
.browse{left:204px;background:linear-gradient(var(--green-top),var(--green-bottom))}
.browse .art{left:16px;top:62px;width:166px;height:82px;background:linear-gradient(#e7ecd8,#c9d1b4)}
.start{left:479px;background:linear-gradient(var(--teal-top),var(--teal-bottom))}
.start .art{left:20px;top:62px;width:160px;height:84px;background:linear-gradient(#5fd3cf,#1e6f82)}
.support{left:754px;background:linear-gradient(var(--orange-top),var(--orange-bottom))}
.support .art{left:15px;top:64px;width:167px;height:76px;background:linear-gradient(#d08a3e,#7a3a12)}
.featured-head{position:absolute;left:140px;top:438px;width:876px;height:31px;border-bottom:3px solid var(--ink)}
.featured-head h3{position:absolute;left:12px;top:2px;font-size:20px;letter-spacing:.8px}
.featured-head a{position:absolute;right:10px;top:8px;font-size:15px;color:var(--ink);letter-spacing:.6px;text-decoration:none}
.venture{position:absolute;width:280px;height:172px;background:var(--tile);border-radius:3px}
.venture h4{position:absolute;left:13px;top:8px;font-size:14.5px;letter-spacing:.9px}
.venture .thumb{position:absolute;left:12px;top:30px;width:80px;height:80px;border:2px solid #8a8a8a;background:#fff}
.venture .thumb i{position:absolute;inset:3px}
.thumb.road i{background:linear-gradient(#9fb2bd,#8b7a5a 55%,#5b5149)}
.thumb.milk i{background:radial-gradient(circle at 50% 50%,#63aef0 60%,#fff 61%)}
.thumb.kids i{background:linear-gradient(135deg,#d9d0c0,#8a8a86 60%,#c9b38e)}
.venture p{position:absolute;left:104px;top:31px;width:156px;font-size:10.5px;line-height:11.6px;color:#111}
.venture .bar{position:absolute;left:14px;top:121px;width:253px;height:17px;border-radius:4px;background:var(--track);
  border:1px solid #b0b0b0;overflow:hidden}
.venture .bar span{display:block;height:100%;border-radius:3px;
  background:repeating-linear-gradient(-60deg,var(--stripe-dark) 0 14px,var(--stripe-light) 14px 26px)}
.venture .stats{position:absolute;left:14px;top:142px;display:flex;font-size:11px;line-height:12px;color:#111}
.venture .stats div{padding-left:5px;height:26px}
.venture .stats div:nth-child(1){width:72px}
.venture .stats div:nth-child(2){width:88px;border-left:1px solid #777;padding-left:20px}
.venture .stats div:nth-child(3){width:90px;border-left:1px solid #777;padding-left:20px}
.col1{left:138px}.col2{left:435px}.col3{left:732px}
.row1{top:488px}.row2{top:675px}
.footer{position:absolute;left:0;top:860px;width:1200px;height:40px;background:var(--navy-deep);
  color:#fff;font-size:16px;text-align:center;line-height:40px;letter-spacing:.3px}
</style>
</head>
<body>
<header class="masthead">
  <div class="brand"><span class="brand-mark"></span><span class="brand-name">Tovel CrowdFunding</span></div>
  <form class="login">
    <div class="field email">Email</div>
    <div class="field password">Password</div>
    <div class="go">Login</div>
  </form>
  <nav class="nav">
    <a class="home" href="#">Home</a>
    <a href="#" style="left:369px">Start a Venture</a>
    <a href="#" style="left:562px">Support a Venture</a>
    <a href="#" style="left:731px">About Us</a>
    <a href="#" style="left:886px">How it works?</a>
  </nav>
</header>

<main class="sheet"></main>

<section class="promo browse">
  <h2>Browse our<br>Ventures</h2>
  <div class="art" role="img" aria-label="Preview of the venture listing"></div>
  <div class="cta">Start Browsing</div>
</section>
<section class="promo start">
  <h2>Start a<br>Venture</h2>
  <div class="art" role="img" aria-label="Illustration of a business team with a rising growth arrow"></div>
  <div class="cta">Start a Venture</div>
</section>
<section class="promo support">
  <h2>Support a<br>Venture</h2>
  <div class="art" role="img" aria-label="Photo of a handshake passing banknotes"></div>
  <div class="cta">Support a Venture</div>
</section>

<div class="featured-head"><h3>Featured Ventures</h3><a href="#">View more ...</a></div>

<article class="venture col1 row1">
  <h4>Start an Adventure with me</h4>
  <div class="thumb road"><i role="img" aria-label="Photo of a traveller jumping on an open road"></i></div>
  <p>Lorem Ipsum is simply dummy text of the printing and typesetting Lorem Ipsum is simply dummy text of the printing and typesetting Lorem Ipsum is simply dummy text</p>
  <div class="bar"><span style="width:81%"></span></div>
  <div class="stats"><div>68%<br>Funded</div><div>$13,789<br>Invested</div><div>13<br>Days to go</div></div>
</article>
<article class="venture col2 row1">
  <h4>Help Identify Milk Quality</h4>
  <div class="thumb milk"><i role="img" aria-label="Project badge image"></i></div>
  <p>Lorem Ipsum is simply dummy text of the printing and typesetting Lorem Ipsum is simply dummy text of the printing and typesetting Lorem Ipsum is simply dummy text</p>
  <div class="bar"><span style="width:63%"></span></div>
  <div class="stats"><div>62%<br>Funded</div><div>$3,456<br>Invested</div><div>4<br>Days to go</div></div>
</article>
<article class="venture col3 row1">
  <h4>Children Learning Methodology</h4>
  <div class="thumb kids"><i role="img" aria-label="Photo of children learning"></i></div>
  <p>Lorem Ipsum is simply dummy text of the printing and typesetting Lorem Ipsum is simply dummy text of the printing and typesetting Lorem Ipsum is simply dummy text</p>
  <div class="bar"><span style="width:96%"></span></div>
  <div class="stats"><div>96%<br>Funded</div><div>$113,789<br>Invested</div><div>1<br>Days to go</div></div>
</article>

<article class="venture col1 row2">
  <h4>Start an Adventure with me</h4>
  <div class="thumb road"><i role="img" aria-label="Photo of a traveller jumping on an open road"></i></div>
  <p>Lorem Ipsum is simply dummy text of the printing and typesetting Lorem Ipsum is simply dummy text of the printing and typesetting Lorem Ipsum is simply dummy text</p>
  <div class="bar"><span style="width:81%"></span></div>
  <div class="stats"><div>68%<br>Funded</div><div>$13,789<br>Invested</div><div>13<br>Days to go</div></div>
</article>
<article class="venture col2 row2">
  <h4>Help Identify Milk Quality</h4>
  <div class="thumb milk"><i role="img" aria-label="Project badge image"></i></div>
  <p>Lorem Ipsum is simply dummy text of the printing and typesetting Lorem Ipsum is simply dummy text of the printing and typesetting Lorem Ipsum is simply dummy text</p>
  <div class="bar"><span style="width:63%"></span></div>
  <div class="stats"><div>62%<br>Funded</div><div>$3,456<br>Invested</div><div>4<br>Days to go</div></div>
</article>
<article class="venture col3 row2">
  <h4>Children Learning Methodology</h4>
  <div class="thumb kids"><i role="img" aria-label="Photo of children learning"></i></div>
  <p>Lorem Ipsum is simply dummy text of the printing and typesetting Lorem Ipsum is simply dummy text of the printing and typesetting Lorem Ipsum is simply dummy text</p>
  <div class="bar"><span style="width:96%"></span></div>
  <div class="stats"><div>96%<br>Funded</div><div>$113,789<br>Invested</div><div>1<br>Days to go</div></div>
</article>

<footer class="footer">© Copyright 12 All Rights Reserved. | Interdum minima venenatis anim interdum lobortis, Disclaimer TOS</footer>
</body>
</html>
```